Wordpress Design Papa Academy Project

Need a homepage design for a wordpress site that is based around becoming a better Dad. The sitemap file and logo file are attached. Navigation should be a combination of horizontal and vertical because the sitemap is extensive. I think the Father's conference, Daddy daughter dance and Essay contest would like nice if they were highlighted in their own rounded boxes at the bottom of the home page perhaps. New design needs to be attention grabbing, colorful but not over the top or too flashy either. I would like the background to be pictures and/or transparent words(similar to this site http://kinhelm.com/). Need a banner image which will be a slider and I need text overlay at the bottom of each image. I like rounded boxes like how this site showcases the news and events sections - http://www.qt.edu/. Need to also incorporate an events calendar, facebook and twitter icons and contact info. A preliminary design was initially created and is attached for you to review. Design needs to be balanced as there is alot of info to display.I have a current site here http://www.papaacad.com/ and you will see why I need a new design.
Updates

Target Market(s)

Dads

Industry/Entity Type

Events

Requirements
Must have
• image slider with text overlay on image, combination of horizontal and vertical navigation, show a dropdown menu under one of the horizontal tabs, events calendar, web safe fonts, colorful, use stock images for any placeholders,footer with sitemap
Nice to have
• rounded boxes, highlight father's conference,daddy daughter dance and essay contest in a separate section from the navigation, also put campus book store and online classes in a vertical nav bar perhaps - maybe in bigger placeholders like stacked boxes or similar.

```html
<!DOCTYPE html>
<html lang="en">
<head>
<meta charset="utf-8">
<title>Papa Academy</title>
<link href="https://fonts.googleapis.com/css2?family=Arimo:wght@400;700&family=Tinos:wght@400;700&display=swap" rel="stylesheet">
<style>
:root{
  --navy:#1c3d72;
  --navy-dark:#132d57;
  --nav-purple:#6b6b9b;
  --lavender:#a9a9c9;
  --header-pink:#dccbcb;
  --rose:#c9b0b4;
  --box-head:#dcc9c9;
  --pink-btn:#e4a0a4;
  --text:#2b2b3a;
  --white:#ffffff;
  --footer:#6f6f9d;
}
*{box-sizing:border-box;margin:0;padding:0}
html,body{width:820px;height:1200px;overflow:hidden}
body{position:relative;background:var(--white);font-family:"Arimo",Arial,sans-serif;color:var(--text)}
.abs{position:absolute}
a{color:inherit;text-decoration:none}

/* header */
.site-header{left:0;top:0;width:820px;height:120px;background:radial-gradient(ellipse at 20% 60%,#f0e6e6 0%,var(--header-pink) 55%,#cfbcbd 100%)}
.brand{left:108px;top:44px;display:flex;align-items:center;gap:12px}
.brand-mark{width:50px;height:50px;border-radius:50%;background:var(--navy)}
.brand-name{font-family:"Tinos","Times New Roman",serif;font-size:27px;color:var(--navy-dark)}
.account-links{left:652px;top:10px;font-size:8px;color:#4b4b5e;letter-spacing:.5px;word-spacing:10px}
.portal-buttons{left:514px;top:32px;width:201px;height:23px;border-radius:6px;background:linear-gradient(#b58e92,#8c6468);display:flex;font-size:8px;color:#f4e4e4;align-items:center;border:1px solid #7c585c}
.portal-buttons span{flex:1;text-align:center}
.portal-buttons span+span{border-left:1px solid #d7c0c2}
.search{left:636px;top:67px;width:79px;height:14px;border-radius:7px;background:#fff;border:1px solid #9c9cb0;font-size:6px;color:#888;padding:3px 8px}
.search-go{right:-2px;top:-3px;width:18px;height:18px;border-radius:50%;background:#59596f;color:#fff;font-size:6px;font-weight:700;text-align:center;line-height:18px}
.feature-tab{top:98px;height:22px;border-radius:6px 6px 0 0;font-size:8px;color:#fff;text-align:center;line-height:22px}
.tab-conference{left:432px;width:96px;background:linear-gradient(#3b5d8d,var(--navy))}
.tab-dance{left:530px;width:94px;background:linear-gradient(#f2c2c4,#dc9c9f)}
.tab-essay{left:634px;width:81px;background:linear-gradient(#a6a6cf,#7b7bae)}

/* nav */
.main-nav{left:0;top:120px;width:820px;height:36px;background:var(--nav-purple)}
.nav-item{top:0;height:36px;line-height:36px;font-size:9px;color:#fff}
.nav-home{left:129px;top:9px;width:33px;height:19px;line-height:19px;text-align:center;background:var(--navy-dark);border-radius:3px;font-weight:700}
.nav-active{left:424px;top:0;width:74px;height:38px;background:#fff;color:var(--navy-dark);text-align:center;border-radius:5px 5px 0 0}

/* hero */
.hero{left:0;top:156px;width:820px;height:382px;background:linear-gradient(#b3b3d1,var(--lavender) 60%,#9d9dc0)}
.hero-letters{left:0;top:156px;width:820px;height:382px}
.dropdown{left:112px;top:156px;width:603px;height:240px;background:#fff;border-radius:0 0 6px 6px;box-shadow:0 2px 4px rgba(0,0,0,.2)}
.side-menu{left:116px;top:168px;width:141px}
.side-menu li{list-style:none;height:22px;margin-bottom:2px;border:1px solid #c6c6e2;border-radius:4px;font-size:7.5px;line-height:21px;padding-left:24px;color:var(--navy-dark)}
.side-menu li.current{background:var(--navy-dark);color:#fff;border-color:var(--navy-dark);border-radius:4px 0 0 4px}
.sub-menu{left:265px;top:168px;width:180px;height:180px;background:var(--navy-dark);border-radius:0 5px 5px 5px;padding:14px 0 0 56px}
.sub-menu li{list-style:none;font-size:7.5px;color:#fff;height:24px}
.info-mark{left:600px;top:283px;width:70px;text-align:center;font-family:"Arimo",Arial,sans-serif;font-size:10px;color:var(--navy-dark);font-weight:700}
.info-mark .dot{display:block;width:40px;height:40px;border-radius:50%;background:var(--navy);margin:0 auto 4px}
.info-title{left:594px;top:358px;font-size:20px;color:var(--navy-dark)}
.slide{left:112px;top:396px;width:603px;height:110px;background:linear-gradient(90deg,#8a6a4e,#a88a6b 40%,#b44a4a 60%,#8a6a52)}
.slide-caption{left:112px;top:438px;width:603px;height:68px;background:rgba(222,212,214,.85)}
.slide-title{left:145px;top:450px;font-family:"Tinos","Times New Roman",serif;font-size:21px;color:var(--navy-dark)}
.slide-text{left:145px;top:477px;font-size:11px;color:var(--navy-dark);letter-spacing:.3px}
.slide-more{left:590px;top:456px;width:86px;height:29px;border-radius:5px;background:linear-gradient(#f0b8ba,#d98d92);color:#fff;font-size:11px;text-align:center;line-height:29px;border:1px solid #c97e83}
.slider-dots{left:386px;top:519px;display:flex;gap:3px}
.slider-dots i{width:7px;height:7px;border-radius:50%;background:#6a7fc4;display:block}

/* cards */
.card{border:2px solid var(--rose);border-radius:8px;background:#fff;overflow:hidden}
.card-head{height:43px;background:var(--box-head);position:relative}
.card-title{position:absolute;left:20px;top:10px;font-size:18px;color:var(--navy-dark)}
.card-copy{font-size:7.5px;line-height:1.45;color:var(--text)}
.about-card{left:109px;top:571px;width:193px;height:190px}
.events-card{left:318px;top:571px;width:191px;height:190px}
.shop-card{left:523px;top:571px;width:194px;height:190px;border-color:#4c4f8c}
.about-logo{position:absolute;left:14px;top:52px;width:64px;height:61px;border:1px solid #7d8fbd;display:flex;align-items:center;justify-content:center;font-size:8px;color:var(--navy-dark);font-weight:700;text-align:center}
.event-row{position:absolute;left:16px;display:flex;gap:16px}
.event-date{width:38px;height:36px;border-radius:6px;background:var(--navy-dark);border:2px solid #9aa5c6;color:#fff;text-align:center;font-size:10px;line-height:1.15;padding-top:4px}
.event-date small{font-size:8px;display:block}
.event-row .card-copy{width:110px;padding-top:6px}
.events-dots{position:absolute;right:18px;top:16px;display:flex;gap:3px}
.events-dots i{width:12px;height:12px;border-radius:50%;border:1px solid #a8a8c0;display:block}
.events-dots i:first-child{background:#9aa1c8}
.view-all{position:absolute;right:18px;bottom:8px;font-size:7px}
.shop-mark{position:absolute;left:18px;top:8px;width:30px;height:30px;border-radius:50%;background:var(--navy)}
.shop-title{position:absolute;left:0;width:100%;top:20px;text-align:center;font-size:18px;color:var(--navy-dark);padding-left:30px}
.product{position:absolute;left:48px;top:52px;width:90px;height:72px;border:1px solid #9fa6cc;background:linear-gradient(#fff,#f6f2f3)}
.product-fill{position:absolute;left:28px;top:6px;width:34px;height:60px;background:linear-gradient(#8a3a55,#5a1f35);border-radius:6px}
.buy{position:absolute;left:96px;top:166px;width:42px;height:14px;border-radius:5px;background:#2d5aa3;color:#fff;font-size:8px;text-align:center;line-height:14px}

.promo-card{top:790px;width:191px;height:255px}
.promo-head{height:42px;background:var(--box-head);position:relative;font-size:8.5px;color:var(--navy-dark);text-align:right;padding:20px 18px 0 0}
.promo-img{height:124px}
.promo-copy{font-size:9.5px;line-height:1.3;color:var(--navy-dark);padding:6px 12px 0 12px}
.promo-more{position:absolute;right:8px;bottom:9px;width:62px;height:24px;border-radius:5px;background:#2a4f8c;color:#fff;font-size:10px;text-align:center;line-height:24px}
.badge-circle{left:104px;top:778px;width:70px;height:70px;border-radius:50%;background:#e8dede;border:2px solid var(--rose);display:flex;align-items:center;justify-content:center;font-size:9px;font-weight:700;color:var(--navy-dark);text-align:center;line-height:1.1}

/* footer */
.site-footer{left:0;top:1078px;width:820px;height:122px;background:var(--footer)}
.footer-col{font-size:7.5px;color:#fff;line-height:1.45}
.footer-mark{left:372px;top:1062px;width:76px;height:76px;border-radius:50%;background:#d9dae8;display:flex;align-items:center;justify-content:center;font-size:9px;font-weight:700;color:var(--navy-dark);text-align:center}
.social{display:flex;gap:3px;margin-top:5px}
.social i{width:11px;height:11px;border-radius:2px;display:block;background:#d4d6e6}
</style>
</head>
<body>

<header class="abs site-header">
  <div class="abs brand"><span class="brand-mark"></span><span class="brand-name">Papa Academy, Inc.</span></div>
  <div class="abs account-links">LOGIN SIGN UP</div>
  <div class="abs portal-buttons"><span>ON LINE CLASSES</span><span>CAMPUS BOOKSTORE</span></div>
  <div class="abs search">search<span class="abs search-go">GO</span></div>
  <div class="abs feature-tab tab-conference">father's conference</div>
  <div class="abs feature-tab tab-dance">daddy daughter dance</div>
  <div class="abs feature-tab tab-essay">essay contest</div>
</header>

<section class="abs hero" role="img" aria-label="Background of faint handwritten letters on lavender"></section>

<nav class="abs main-nav">
  <span class="abs nav-item nav-home">Home</span>
  <span class="abs nav-item" style="left:202px">About</span>
  <span class="abs nav-item" style="left:270px">Contact</span>
  <span class="abs nav-item" style="left:350px">Admissions</span>
  <span class="abs nav-item nav-active">Information</span>
  <span class="abs nav-item" style="left:526px">Services</span>
  <span class="abs nav-item" style="left:600px">Products</span>
  <span class="abs nav-item" style="left:680px">Blog</span>
</nav>

<div class="abs dropdown"></div>
<ul class="abs side-menu">
  <li class="current">Education center</li>
  <li>Parenting Classes</li>
  <li>Online parenting classes</li>
  <li>Divorced Dads</li>
  <li>Single Dads</li>
  <li>News and Announcements</li>
  <li>Library</li>
  <li>Resource Center</li>
  <li>Legal information</li>
</ul>
<ul class="abs sub-menu">
  <li>Orientation (0 -5)</li>
  <li>Freshman (6 -9)</li>
  <li>Sophomore (10- 13)</li>
  <li>Junior (14 – 17)</li>
  <li>Senior (18 and over)</li>
  <li>Alumni ( Mentors)</li>
</ul>
<div class="abs info-mark"><span class="dot"></span>Papa Academy</div>
<div class="abs info-title">Information</div>

<div class="abs slide" role="img" aria-label="Slide photo: child in a red raincoat among autumn leaves"></div>
<div class="abs slide-caption"></div>
<div class="abs slide-title">Jujubes jelly beans pastry</div>
<div class="abs slide-text">cake biscuit jujubes oat cake. Candy canes candy canes topping lemon...</div>
<a class="abs slide-more">more &gt;&gt;</a>
<div class="abs slider-dots"><i></i><i></i><i></i><i></i></div>

<section class="abs card about-card">
  <div class="card-head"><span class="card-title">About</span></div>
  <div class="about-logo">Papa<br>Academy</div>
  <p class="card-copy" style="position:absolute;left:86px;top:52px;width:96px">Jujubes jelly beans pastry cake biscuit jujubes oat cake. Candy canes candy canes topping lemon drops liquorice. Faworki chocolate bar cookie tart powder</p>
  <p class="card-copy" style="position:absolute;left:14px;top:118px;width:170px">Jujubes jelly beans pastry cake biscuit jujubes oat cake. Candy canes candy canes topping lemon drops liquorice. Faworki chocolate bar cookie tart powder tootsie roll macaroon liquorice. Bonbon fruitcake croissant. Danish sugar plum</p>
</section>

<section class="abs card events-card">
  <div class="card-head"><span class="card-title">Events</span><div class="events-dots"><i></i><i></i><i></i></div></div>
  <div class="event-row" style="top:50px"><div class="event-date">12<small>DEC</small></div><p class="card-copy">Jujubes jelly beans pastry cake biscuit jujubes oat</p></div>
  <div class="event-row" style="top:92px"><div class="event-date">01<small>DEC</small></div><p class="card-copy">Jujubes jelly beans pastry cake biscuit jujubes oat</p></div>
  <div class="event-row" style="top:134px"><div class="event-date">25<small>NOV</small></div><p class="card-copy">Jujubes jelly beans pastry cake biscuit jujubes oat</p></div>
  <a class="view-all">View all</a>
</section>

<section class="abs card shop-card">
  <span class="shop-mark"></span>
  <div class="shop-title">Shop</div>
  <div class="product" role="img" aria-label="Product photo: maroon sweatshirt"><span class="product-fill"></span></div>
  <p class="card-copy" style="position:absolute;left:48px;top:128px;width:100px">Jujubes jelly beans pastry cake biscuit jujubes oat</p>
  <span style="position:absolute;left:116px;top:150px;font-size:10px">25 $</span>
  <a class="buy">Buy</a>
  <svg style="position:absolute;right:8px;top:82px" width="12" height="30" viewBox="0 0 12 30"><path d="M2 2 L10 15 L2 28" fill="none" stroke="#e1d2d2" stroke-width="3"/></svg>
</section>

<section class="abs card promo-card" style="left:115px">
  <div class="promo-head">Father's Conference</div>
  <div class="promo-img" role="img" aria-label="Illustration: workers lifting a giant light bulb" style="background:linear-gradient(#f3efd2,#ece6c0)"></div>
  <p class="promo-copy">Jujubes jelly beans pastry<br>cake biscuit jujubes oat cake. Candy canes candy canes topping lemon...</p>
  <a class="promo-more">more &gt;&gt;</a>
</section>
<div class="abs badge-circle">Papa<br>Academy</div>

<section class="abs card promo-card" style="left:319px">
  <div class="promo-head">My Dad Essay Contest
    <svg style="position:absolute;left:26px;top:8px" width="30" height="28" viewBox="0 0 30 28"><rect x="2" y="5" width="20" height="20" rx="2" fill="none" stroke="#1c3d72" stroke-width="3"/><path d="M12 17 L25 3 L28 6 L15 20 L11 21 Z" fill="#1c3d72"/></svg>
  </div>
  <div class="promo-img" role="img" aria-label="Photo: father and young son smiling" style="background:linear-gradient(135deg,#6b6f5a,#b9a58d 50%,#4f5d48)"></div>
  <p class="promo-copy">Jujubes jelly beans pastry<br>cake biscuit jujubes oat cake. Candy canes candy canes topping lemon...</p>
  <a class="promo-more">more &gt;&gt;</a>
</section>

<section class="abs card promo-card" style="left:524px">
  <div class="promo-head">Daddy Daughter Dance
    <svg style="position:absolute;left:26px;top:4px" width="26" height="34" viewBox="0 0 26 34"><ellipse cx="8" cy="9" rx="6" ry="8" fill="#1c3d72"/><ellipse cx="18" cy="11" rx="6" ry="8" fill="#1c3d72"/><path d="M8 17 L12 33 M18 19 L12 33" stroke="#1c3d72" stroke-width="1"/></svg>
  </div>
  <div class="promo-img" role="img" aria-label="Photo: little girl in red raincoat sitting in autumn leaves" style="background:linear-gradient(135deg,#6e5a43,#a7896a 45%,#b8413f 55%,#7a6149)"></div>
  <p class="promo-copy">Jujubes jelly beans pastry<br>cake biscuit jujubes oat cake. Candy canes candy canes topping lemon...</p>
  <a class="promo-more">more &gt;&gt;</a>
</section>

<footer class="abs site-footer">
  <div class="abs footer-col" style="left:114px;top:14px">Home<br>About<br>Contact<br>Admissions<br>Information<br>Services<br>Products<br>Blog</div>
  <div class="abs footer-col" style="left:211px;top:14px"><b style="font-size:8.5px">Papa Academy</b><br><b>Adress:</b> Jujubes jelly beans 15<br><b>Tel.:</b> 99 99999
    <div style="margin-top:16px">Follow PA on:</div>
    <div class="social"><i></i><i></i><i></i><i></i><i></i></div>
  </div>
  <div class="abs footer-col" style="left:502px;top:14px">On line Courses<br>Campus Bookstore<br><br><br>Father's Conference<br>Essay Contest<br>Daddy Daughter Dance</div>
  <div class="abs footer-col" style="left:632px;top:14px">Father's Conference<br>Essay Contest<br>Daddy Daughter Dance<br>Father's Conference<br>Essay Contest<br>Daddy Daughter Dance</div>
</footer>
<div class="abs footer-mark">Papa<br>Academy</div>

</body>
</html>
```